VORK Business Cards, Letterhead and Envelopes
Business Cards, Letterhead and Envelopes
Simple
Rajendran P Subbiah
Dirección TI - ERP Quandrel
Calle Tepozan 58,
Col. Las Brisas,
Distrito Federal
Mexico - 04260
rajen@vorkitel.mx
www.vorkitel.mx, www.vorkitel.in

```html
<!DOCTYPE html>
<html lang="en">
<head>
<meta charset="utf-8">
<title>VORK Stationery</title>
<link href="https://fonts.googleapis.com/css2?family=Open+Sans:wght@400;600;700&family=Tinos:wght@400&display=swap" rel="stylesheet">
<style>
:root{
  --blue:#1d62bf;
  --blue-deep:#17409a;
  --blue-light:#3d94e0;
  --silver:#c4c8cd;
  --silver-dark:#8a9098;
  --grey-card:#8d9096;
  --grey-card-dark:#6d7075;
  --ink:#2a2a2a;
  --paper:#ffffff;
  --edge:#d7d9dc;
}
*{box-sizing:border-box;margin:0;padding:0}
html,body{width:1200px;height:773px;overflow:hidden;background:var(--paper)}
.canvas{position:relative;width:1200px;height:773px;overflow:hidden;background:var(--paper);font-family:"Open Sans",Arial,sans-serif}
.sheet{position:absolute;background:var(--paper);border:1px solid var(--edge);overflow:hidden}
.brand{position:absolute;display:flex;align-items:center;gap:8px;font-family:"Open Sans",Arial,sans-serif;font-weight:700;color:var(--blue);white-space:nowrap;letter-spacing:.5px}
.brand-mark{display:block;background:var(--blue);flex:none}
.brand.on-dark{color:#fff}
.brand.on-dark .brand-mark{background:#fff}
.serif{font-family:"Tinos","Times New Roman",serif}

/* Plain footer bands */
.band-silver,.band-blue{position:absolute;left:0;width:100%}
.band-silver{background:linear-gradient(90deg,var(--silver-dark),#e3e6e9 50%,var(--silver-dark))}
.band-blue{background:linear-gradient(90deg,#1a56b0,#2c7fd3 60%,var(--blue))}

/* Letterhead */
.letterhead{left:43px;top:24px;width:514px;height:698px}
.letterhead .brand{left:26px;top:50px;font-size:26px}
.letterhead .brand-mark{width:28px;height:28px}
.letterhead .band-silver{bottom:100px;height:34px}
.letterhead .band-blue{bottom:0;height:96px}
.letterhead .footer-contact{position:absolute;left:22px;bottom:10px;color:#fff;font-size:9.5px;line-height:12px}

/* Business cards */
.card{position:absolute;overflow:hidden}
.card-front{left:576px;top:46px;width:230px;height:122px;background:var(--paper);border:1px solid var(--edge)}
.card-front .brand{left:10px;top:10px;font-size:13px;gap:5px}
.card-front .brand-mark{width:12px;height:12px}
.card-front .holder{position:absolute;right:10px;top:12px;text-align:right;color:var(--ink)}
.card-front .holder-name{font-size:8px;font-weight:600}
.card-front .holder-role{font-size:6px;margin-top:2px}
.card-front .band-blue{top:50px;height:7px}
.card-front .band-silver{top:59px;height:4px}
.card-front .card-contact{position:absolute;left:10px;bottom:9px;font-size:6px;line-height:8px;color:var(--ink)}
.card-logo-white{left:821px;top:53px;width:216px;height:120px;background:var(--paper);border:1px solid var(--edge)}
.card-logo-white .brand{left:50px;top:46px;font-size:20px}
.card-logo-white .brand-mark{width:18px;height:18px}
.card-blue{left:576px;top:192px;width:192px;height:108px;background:linear-gradient(135deg,var(--blue-light),var(--blue) 55%,var(--blue-deep))}
.card-blue .brand{left:40px;top:40px;font-size:20px}
.card-blue .brand-mark{width:18px;height:18px}
.card-grey-back{left:912px;top:192px;width:192px;height:132px;background:linear-gradient(150deg,var(--grey-card),var(--grey-card-dark));box-shadow:0 2px 4px rgba(0,0,0,.25)}
.card-grey-back .plain-square{position:absolute;left:84px;top:52px;width:24px;height:24px;background:#fff}
.card-grey{left:758px;top:252px;width:178px;height:120px;background:linear-gradient(150deg,#9da0a5,var(--grey-card-dark));box-shadow:0 2px 5px rgba(0,0,0,.3)}
.card-grey .brand{left:26px;top:46px;font-size:19px}
.card-grey .brand-mark{width:17px;height:17px}

/* Envelope */
.envelope{left:571px;top:384px;width:538px;height:348px}
.envelope .flap{position:absolute;left:0;top:0;width:100%;height:84px;background:linear-gradient(90deg,var(--blue-light),#2a6fcc 50%,#2a3aa8)}
.envelope .flap .plain-square{position:absolute;left:258px;top:30px;width:22px;height:22px;background:#fff}
.envelope .brand{left:12px;top:112px;font-size:24px}
.envelope .brand-mark{width:24px;height:24px}
.envelope .sender{position:absolute;left:12px;top:166px;font-size:10px;line-height:12px;color:var(--ink)}
.envelope .band-silver{bottom:66px;height:30px}
.envelope .band-blue{bottom:0;height:62px}
</style>
</head>
<body>
<main class="canvas">

  <section class="sheet letterhead" aria-label="Letterhead">
    <div class="brand"><span class="brand-mark"></span>VORK TECHNOLOGIES</div>
    <div class="band-silver"></div>
    <div class="band-blue"></div>
    <div class="footer-contact serif">
      Calle Tepozan 58, Col. Las Brisas,<br>
      Distrito Federal, Mexico - 04260<br>
      Phone: +52 (55) 4810 2274 | +91 (44) 4417 3390<br>
      Email: rajen@vorkitel.mx, www.vorkitel.mx, www.vorkitel.in
    </div>
  </section>

  <section class="card card-front" aria-label="Business card front">
    <div class="brand"><span class="brand-mark"></span>VORK</div>
    <div class="holder">
      <div class="holder-name">Rajendran P Subbiah</div>
      <div class="holder-role">Dirección TI - ERP Quandrel</div>
    </div>
    <div class="band-blue"></div>
    <div class="band-silver"></div>
    <div class="card-contact serif">
      Calle Tepozan 58, Col. Las Brisas, Distrito Federal<br>
      Mexico - 04260 | Ph: +52 (55) 4810 2274<br>
      rajen@vorkitel.mx, www.vorkitel.mx, www.vorkitel.in
    </div>
  </section>

  <section class="card card-logo-white" aria-label="Business card back">
    <div class="brand"><span class="brand-mark"></span>VORK</div>
  </section>

  <section class="card card-blue" aria-label="Business card blue back">
    <div class="brand on-dark"><span class="brand-mark"></span>VORK</div>
  </section>

  <section class="card card-grey-back" aria-label="Business card dark grey">
    <span class="plain-square"></span>
  </section>

  <section class="card card-grey" aria-label="Business card grey">
    <div class="brand on-dark"><span class="brand-mark"></span>VORK</div>
  </section>

  <section class="sheet envelope" aria-label="Envelope">
    <div class="flap"><span class="plain-square"></span></div>
    <div class="brand"><span class="brand-mark"></span>VORK TECHNOLOGIES</div>
    <div class="sender serif">
      Calle Tepozan 58, Col. Las Brisas,<br>
      Distrito Federal, Mexico - 04260
    </div>
    <div class="band-silver"></div>
    <div class="band-blue"></div>
  </section>

</main>
</body>
</html>
```